Lantern Method of Ascent Programme Graphic

Please refer to attached graphic.
I wish to redesign this graphic to represent a programme of work that we (Vendro) deliver to our customers.
The design represents 9 steps ( 3 steps at each of 3 levels) and is all about implementing the 'Lantern Method of Ascent'

I like the fact that the increasing business growth is evident when you are progressing through the stages, but the current graphic looks dated and the colours are not working.
I would also like to incorporate the LMA logo we have created.

Target Market(s)

IT Sector - businesses looking to grow

Industry/Entity Type

We are a digital marketing company

Requirements
Must have
• Clear, concise design
Should not have
• Design must not be complicated

```html
<!DOCTYPE html>
<html lang="en">
<head>
<meta charset="utf-8">
<title>Lantern Method of Ascent</title>
<link rel="stylesheet" href="https://fonts.googleapis.com/css2?family=Oswald:wght@500;600&display=swap">
<style>
  :root {
    --navy: #24286a;
    --navy-deep: #1d2160;
    --royal: #1657b7;
    --sky: #1b9ad7;
    --sky-soft: #7b97c9;
    --pipe: #2b8ed6;
    --plinth-top: #3443a2;
    --glow: #4fc6ef;
    --white: #ffffff;
  }
  html, body { margin: 0; padding: 0; overflow: hidden; background: var(--white); }
  .canvas { width: 1200px; height: 848px; position: relative; overflow: hidden; }
  .canvas svg { display: block; }
  .label { font-family: "Oswald", "Arial Narrow", sans-serif; font-weight: 600; fill: var(--white); }
  .step-item { font-size: 27px; letter-spacing: 0.2px; }
  .step-number { font-size: 52px; }
  .band-title { font-size: 24px; letter-spacing: 1px; }
  .plaque-title { font-size: 19px; }
  .plaque-sub { font-size: 11.5px; font-weight: 500; letter-spacing: 0.4px; }
  .method-title { font-size: 44px; letter-spacing: 1px; }
  .brand-name { font-size: 40px; fill: var(--sky); }
  .icon-line { fill: none; stroke: var(--white); stroke-width: 2.2; stroke-linecap: round; stroke-linejoin: round; }
  .icon-fill { fill: var(--white); }
  .pipe { fill: none; stroke: var(--pipe); stroke-width: 6; stroke-linejoin: round; }
  .pipe-core { fill: none; stroke: var(--navy); stroke-width: 2.5; stroke-linejoin: round; }
</style>
</head>
<body>
<div class="canvas">
<svg width="1200" height="848" viewBox="0 0 1200 848" xmlns="http://www.w3.org/2000/svg">
  <defs>
    <linearGradient id="pillarFill" x1="0" y1="0" x2="0" y2="1">
      <stop offset="0" stop-color="#1763c4"/>
      <stop offset="1" stop-color="#222a66"/>
    </linearGradient>
    <linearGradient id="glowFill" x1="0" y1="0" x2="0" y2="1">
      <stop offset="0" stop-color="#3fb5ea"/>
      <stop offset="1" stop-color="#9ee3f8"/>
    </linearGradient>
  </defs>

  <!-- floor glow -->
  <polygon points="178,788 1022,788 1200,848 0,848" fill="url(#glowFill)"/>

  <!-- connecting pipes -->
  <g class="connectors">
    <path class="pipe" d="M222 420 H196 V626 H1000 V575 H985"/>
    <path class="pipe-core" d="M222 420 H196 V626 H1000 V575 H985"/>
    <path class="pipe" d="M438 420 H455 V605 H473 V420 H493"/>
    <path class="pipe" d="M438 498 H493 M438 575 H493"/>
    <path class="pipe" d="M712 420 H728 V605 H746 V420 H765"/>
    <path class="pipe" d="M712 498 H765 M712 575 H765"/>
    <path class="pipe-core" d="M438 420 H455 V605 H473 V420 H493 M712 420 H728 V605 H746 V420 H765"/>
  </g>

  <!-- step 1 -->
  <g class="pillar pillar-one">
    <polygon points="220,340 438,268 438,640 220,640" fill="url(#pillarFill)"/>
    <path d="M220 250 Q220 240 230 244 L332 300 L220 338 Z" fill="var(--navy)"/>
    <text class="label step-number" x="232" y="312">1</text>
    <polygon points="220,342 438,268 438,306 220,380" fill="var(--sky)"/>
    <text class="label band-title" transform="translate(262,356) rotate(-18.5)">LANTERN</text>
  </g>

  <!-- step 2 -->
  <g class="pillar pillar-two">
    <polygon points="493,245 712,173 712,640 493,640" fill="url(#pillarFill)"/>
    <path d="M493 158 Q493 148 503 152 L610 205 L493 243 Z" fill="var(--sky)"/>
    <text class="label step-number" x="505" y="218">2</text>
    <polygon points="493,247 712,173 712,215 493,289" fill="var(--sky-soft)"/>
    <text class="label band-title" transform="translate(530,262) rotate(-18.5)">METHOD</text>
  </g>

  <!-- step 3 -->
  <g class="pillar pillar-three">
    <polygon points="765,150 985,75 985,640 765,640" fill="url(#pillarFill)"/>
    <path d="M765 73 Q765 63 775 67 L880 118 L765 150 Z" fill="var(--royal)"/>
    <text class="label step-number" x="777" y="128">3</text>
    <polygon points="765,150 985,75 985,115 765,190" fill="var(--navy)"/>
    <text class="label band-title" transform="translate(800,162) rotate(-18.5)">ASCENT</text>
  </g>

  <!-- item tags -->
  <g class="items">
    <g fill="var(--navy)">
      <polygon points="212,404 255,404 263,421 255,438 212,438"/>
      <polygon points="212,482 255,482 263,499 255,516 212,516"/>
      <polygon points="212,558 255,558 263,575 255,592 212,592"/>
    </g>
    <g fill="#3d71c4">
      <polygon points="486,404 529,404 537,421 529,438 486,438"/>
      <polygon points="486,482 529,482 537,499 529,516 486,516"/>
      <polygon points="486,558 529,558 537,575 529,592 486,592"/>
    </g>
    <g fill="#1e66c6">
      <polygon points="758,404 801,404 809,421 801,438 758,438"/>
      <polygon points="758,482 801,482 809,499 801,516 758,516"/>
      <polygon points="758,558 801,558 809,575 801,592 758,592"/>
    </g>

    <!-- icons -->
    <g class="icon-fill">
      <circle cx="228" cy="415" r="4"/><circle cx="236" cy="413" r="4.5"/><circle cx="244" cy="415" r="4"/>
      <path d="M220 428 Q228 418 236 424 Q244 418 252 428 Z"/>
      <ellipse cx="236" cy="490" rx="9" ry="3.5"/>
      <path d="M227 493 V506 Q236 511 245 506 V493 Q236 498 227 493 Z"/>
      <path d="M498 412 H524 V428 H507 L501 433 V428 H498 Z"/>
    </g>
    <circle class="icon-line" cx="236" cy="575" r="5"/>
    <circle class="icon-line" cx="236" cy="575" r="10" stroke-dasharray="4 3.2"/>
    <g fill="#3d71c4"><circle cx="505" cy="420" r="1.6"/><circle cx="511" cy="420" r="1.6"/><circle cx="517" cy="420" r="1.6"/></g>
    <circle class="icon-line" cx="510" cy="499" r="10"/>
    <path class="icon-line" d="M505 499 L509 503 L516 495"/>
    <path class="icon-line" d="M503 568 H516 Q518 568 518 571 L503 579 Q501 582 504 582 H517"/>
    <path class="icon-line" d="M771 428 L778 420 L783 424 L792 414 M786 414 H792 V420"/>
    <path class="icon-line" d="M782 508 V496 M782 498 Q775 498 774 491 Q781 490 782 498 M782 496 Q789 495 790 489 Q783 489 782 496"/>
    <path class="icon-fill" d="M774 504 H790 L788 512 H776 Z"/>
    <path class="icon-line" d="M774 565 H786 L791 570 V586 H774 Z M778 574 L784 580 M784 576 V580 H780"/>

    <g class="label step-item">
      <text x="270" y="432">PERSONAS</text>
      <text x="268" y="510">DATABASE</text>
      <text x="266" y="586">SYSTEMS</text>
      <text x="550" y="432">MESSAGING</text>
      <text x="550" y="510">LEADS</text>
      <text x="550" y="586">PIPELINE</text>
      <text x="823" y="432">SALES</text>
      <text x="823" y="510">NURTURE</text>
      <text x="823" y="586">REFERENCE</text>
    </g>
  </g>

  <!-- plaques -->
  <g class="plaques">
    <rect x="208" y="642" width="237" height="58" fill="var(--sky)"/>
    <rect x="483" y="642" width="235" height="58" fill="var(--sky)"/>
    <rect x="756" y="642" width="235" height="58" fill="var(--sky)"/>
    <g class="label" text-anchor="middle">
      <text class="plaque-title" x="326" y="672">NUMBERS THAT MATTER</text>
      <text class="plaque-sub" x="326" y="690">FOUNDATION METRICS</text>
      <text class="plaque-title" x="600" y="672">WEEKLY SCORECARD</text>
      <text class="plaque-sub" x="600" y="690">TACTICAL EXECUTION</text>
      <text class="plaque-title" x="873" y="672">MONTHLY SCORECARD</text>
      <text class="plaque-sub" x="873" y="690">STRATEGIC REVIEW</text>
    </g>
  </g>

  <!-- plinth -->
  <g class="plinth">
    <polygon points="190,700 1010,700 1022,712 178,712" fill="var(--plinth-top)"/>
    <rect x="178" y="712" width="844" height="76" fill="var(--navy-deep)"/>
    <rect x="193" y="727" width="46" height="46" fill="none" stroke="var(--sky)" stroke-width="3"/>
    <text class="label" x="216" y="757" text-anchor="middle" font-size="16">LMA</text>
    <text class="label method-title" x="262" y="770">LANTERN METHOD OF ASCENT</text>
    <text class="label brand-name" x="880" y="768">VENDRO</text>
  </g>
</svg>
</div>
</body>
</html>
```